Brandomir tile letterhead contractor

I would like to get a very good expressive letterhead or resume with great 3D design as a tile contractor company offering my services to others tile companies, general contractors and home owners clients. (This is the idea)
Founder/owner.
“Proud to represent and provide my life’s passion services as brandomir tile.”
I’m journeyman setter, I have passion for creating visually stunning designs with a focus on creativity usability. I have been working as setter with a remarkable companies for over 20 years and I specialize in commercial and residential projects.
My experience and expertise have enabled me to create beautiful master pieces for a wide range of clients, from a small businesses to a large corporations.
My first goal in any project that you hire me for is to provide a professional and high-quality product that meets and exceeds your expectations. You can really assured that I will strive tirelessly to produce the best results for our clients until the final project is done.
*My team will move forward with your needs in every step we walk together
*We have a very solid foundations knowledge altogether rely in the best equipment possible to make (builds)what it takes with best quality possible
*I’m an independent contractor and beaten to another prestigious companies …. ETC. ETC.
ILL TRY TO KEEP UPDATING MORE INFO.
Target Market(s)
General contractors, tile companies and home owners builders
Industry/Entity Type
Tile construction
Look and feel

```html
<!DOCTYPE html>
<html lang="en">
<head>
<meta charset="utf-8">
<title>Brandomir Tile — Letterhead</title>
<link href="https://fonts.googleapis.com/css2?family=Open+Sans:wght@400;600&family=Roboto:wght@400&display=swap" rel="stylesheet">
<style>
  :root {
    --backdrop: #dcdcdc;
    --paper: #f7f7f7;
    --brand: #4a2c2e;
    --band: #553537;
    --rule: #111111;
    --body-text: #6a6a6a;
    --band-text: #ffffff;
    --ink-placeholder: #dfe2e8;
  }
  * { margin: 0; padding: 0; box-sizing: border-box; }
  html, body {
    width: 1153px;
    height: 1200px;
    overflow: hidden;
    background: var(--backdrop);
  }
  .letterhead {
    position: absolute;
    left: 176px;
    top: 42px;
    width: 800px;
    height: 1116px;
    background: var(--paper);
  }
  .brand {
    position: absolute;
    top: 118px;
    left: 0;
    width: 100%;
    text-align: center;
    font-family: "Open Sans", sans-serif;
  }
  .brand-name {
    color: var(--brand);
    font-size: 26px;
    font-weight: 600;
    letter-spacing: 0.5px;
    line-height: 1.1;
  }
  .brand-tagline {
    margin-top: 6px;
    color: var(--body-text);
    font-size: 12px;
    font-weight: 400;
    letter-spacing: 0.3px;
  }
  .letter {
    position: absolute;
    left: 79px;
    top: 279px;
    width: 642px;
    font-family: "Open Sans", sans-serif;
    font-size: 14.1px;
    line-height: 21px;
    color: var(--body-text);
  }
  .letter p { margin-bottom: 21px; text-align: justify; }
  .letter .salutation, .letter .closing { text-align: left; }
  .signature {
    width: 94px;
    height: 84px;
    margin-top: 16px;
    border-radius: 4px;
    background: linear-gradient(135deg, var(--ink-placeholder), #eef0f3);
  }
  .footer-rule {
    position: absolute;
    left: 0;
    top: 1034px;
    width: 100%;
    height: 3px;
    background: var(--rule);
  }
  .footer {
    position: absolute;
    left: 0;
    top: 1041px;
    width: 100%;
    height: 75px;
    background: var(--band);
    color: var(--band-text);
    font-family: "Roboto", sans-serif;
    font-size: 16.5px;
    display: flex;
    justify-content: space-between;
    padding: 14px 79px 0;
  }
  .contact-list { list-style: none; }
  .contact-list li {
    display: flex;
    align-items: center;
    gap: 7px;
    height: 23px;
  }
  .contact-list.right li { justify-content: flex-end; }
  .icon { width: 16px; height: 16px; fill: var(--band-text); flex: none; }
</style>
</head>
<body>
  <main class="letterhead">
    <header class="brand">
      <div class="brand-name">Brandomir Tile</div>
      <div class="brand-tagline">Set with care, built to last</div>
    </header>

    <article class="letter">
      <p class="salutation">Dear customer,</p>
      <p>Lorem ipsum dolor sit amet, consectetur adipisicing elit, sed do eiusmod tempor incididunt ut labore et dolore magna aliqua. Ut enim ad minim veniam, quis nostrud exercitation ullamco laboris nisi ut aliquip ex ea commodo consequat. Duis aute irure dolor in reprehenderit in voluptate velit esse cillum dolore eu fugiat nulla pariatur. Excepteur sint occaecat cupidatat non proident, sunt in culpa qui officia deserunt mollit anim id est laborum.</p>
      <p>Lorem ipsum dolor sit amet, consectetur adipisicing elit, sed do eiusmod tempor incididunt ut labore et dolore magna aliqua. Ut enim ad minim veniam, quis nostrud exercitation ullamco laboris nisi ut aliquip ex ea commodo consequat. Duis aute irure dolor in reprehenderit in voluptate velit esse cillum dolore eu fugiat nulla pariatur. Excepteur sint occaecat cupidatat non proident, sunt in culpa qui officia deserunt mollit anim id est laborum.</p>
      <p>Lorem ipsum dolor sit amet, consectetur adipisicing elit, sed do eiusmod tempor incididunt ut labore et dolore magna aliqua. Ut enim ad minim veniam, quis nostrud exercitation ullamco laboris nisi ut aliquip ex ea commodo consequat. Duis aute irure dolor in reprehenderit in voluptate velit esse cillum dolore eu fugiat nulla pariatur. Excepteur sint occaecat cupidatat non proident, sunt in culpa qui officia deserunt mollit anim id est laborum.</p>
      <p>Lorem ipsum dolor sit amet, consectetur adipisicing elit, sed do eiusmod tempor incididunt ut labore et dolore magna aliqua. Ut enim ad minim veniam, quis nostrud exercitation ullamco laboris nisi ut aliquip ex ea commodo consequat. Duis aute irure dolor in reprehenderit.</p>
      <p class="closing">Yours Sincerely,</p>
      <div class="signature" role="img" aria-label="Handwritten signature of the sender"></div>
    </article>

    <div class="footer-rule"></div>
    <footer class="footer">
      <ul class="contact-list left">
        <li>
          <svg class="icon" viewBox="0 0 16 16" aria-hidden="true"><path d="M2 6c0-2 3-3.5 6-3.5S14 4 14 6l-2.4.6-.5-1.6c-2-.6-4.2-.6-6.2 0l-.5 1.6zM5 7h6l2 6H3zm3 1.6a1.9 1.9 0 100 3.8 1.9 1.9 0 000-3.8z"/></svg>
          <span>(555) 214-7380</span>
        </li>
        <li>
          <svg class="icon" viewBox="0 0 16 16" aria-hidden="true"><path d="M1 4h14v.8L8 9 1 4.8zM1 6.3l7 4.2 7-4.2V13H1z"/></svg>
          <span>hello@brandomirtile.com</span>
        </li>
      </ul>
      <ul class="contact-list right">
        <li>
          <span>www.brandomirtile.com</span>
          <svg class="icon" viewBox="0 0 16 16" aria-hidden="true"><rect x="1" y="1" width="14" height="14" rx="2"/></svg>
        </li>
        <li>
          <span>Cedar Ridge, 00000</span>
          <svg class="icon" viewBox="0 0 16 16" aria-hidden="true"><path d="M8 0a5.5 5.5 0 00-5.5 5.5C2.5 10 8 16 8 16s5.5-6 5.5-10.5A5.5 5.5 0 008 0zm0 3.3a2.2 2.2 0 110 4.4 2.2 2.2 0 010-4.4z"/></svg>
        </li>
      </ul>
    </footer>
  </main>
</body>
</html>
```